Financing service for small businesses

Need a flyer design promoting our Financing Service, look at the attachment to see the services we offer.
We are a CPA firm and provide a wide range of services including advisory services to small businesses that are trying to obtain bank financing.
The flyer should grab the attention of prospective businesses who need assistant with their financing needs.

Target Market(s)

Small Businesses

Industry/Entity Type

It Service

Font styles to use
Serif

Colors

Designer to choose colors to be used in the design.

Requirements
Must have
• Our Logo and address
• Why use our services
• Look Professional

```html
<!DOCTYPE html>
<html lang="en">
<head>
<meta charset="utf-8">
<title>Business Financing Services Flyer</title>
<link rel="stylesheet" href="https://fonts.googleapis.com/css2?family=Noto+Serif:wght@400;700&display=swap">
<style>
:root{
  --blue:#1f6fb2;
  --blue-dark:#175a93;
  --blue-bright:#1d8ad8;
  --blue-light:#2b93d8;
  --ink:#4a4a4a;
  --grey:#8a8a8a;
  --grey-dark:#3d3d3f;
  --canvas:#e4e4e4;
  --white:#fff;
}
*{margin:0;padding:0;box-sizing:border-box}
html,body{width:1200px;height:1000px;overflow:hidden}
body{background:var(--canvas);font-family:"Noto Serif",Georgia,serif;color:var(--ink);position:relative}
.page{position:absolute;top:142px;width:556px;height:716px;overflow:hidden}
.page--front{left:35px;background:linear-gradient(180deg,#e2e3e5 0%,#f1f1f1 45%,#e9e9ea 100%)}
.page--back{left:610px;background:var(--white)}
.abs{position:absolute}
.curves{position:absolute;left:0;top:0;width:556px;height:716px}

/* front */
.title{left:14px;top:56px;width:240px;text-align:center;font-weight:700;font-size:34px;line-height:1.1;color:var(--blue)}
.title .band{display:block;background:var(--blue);color:var(--white);margin:2px 0;padding:2px 0}
.cities{left:15px;top:180px;font-size:11px;letter-spacing:4.4px;color:var(--ink)}
.intro{left:14px;top:203px;width:244px;font-size:9.4px;line-height:1.27;letter-spacing:-.1px;color:var(--blue)}
.purpose-box{left:15px;top:250px;width:235px;height:48px;background:var(--blue);color:var(--white);font-weight:700;font-size:11px;text-align:center;line-height:1.35;padding-top:9px}
.purposes{left:12px;top:316px;width:245px;list-style:none}
.purposes li{margin-bottom:12px}
.purposes b{display:block;color:var(--blue);font-size:14.5px;line-height:1.2}
.purposes b::before{content:"• "}
.purposes span{display:block;font-size:9.6px;line-height:1.25;padding-left:13px;color:var(--ink)}
.logo{display:flex;align-items:center;gap:6px}
.logo .mark{width:44px;height:44px;background:var(--blue);flex:none}
.logo .name{font-size:11.5px;line-height:1.15;color:var(--blue);letter-spacing:.3px}
.logo--front{left:270px;top:90px}
.photo{background:linear-gradient(135deg,#dfe6ee,#b7c6d6 55%,#8aa0b8)}
.photo--desk{left:270px;top:250px;width:286px;height:190px}
.advisor{left:270px;top:441px;width:286px;height:96px;background:var(--blue-bright);color:var(--white);text-align:center;font-size:10.6px;line-height:1.3;padding:10px 12px}
.advisor b{font-weight:700}
.notch{width:0;height:0;border-left:13px solid transparent;border-right:13px solid transparent;border-top:13px solid var(--blue-bright)}
.notch--advisor{left:400px;top:536px}
.goals{left:270px;top:560px;width:270px;list-style:none}
.goals li{font-size:10.6px;font-weight:700;line-height:1.3;color:var(--ink);padding-left:11px;text-indent:-11px}
.goals li::before{content:"● ";font-size:8px}
.goals span{display:block;font-weight:400;font-size:9.4px;text-indent:0;line-height:1.2}

/* back */
.types-head{left:12px;top:20px;font-size:21px;font-weight:700;color:var(--grey)}
.types-head .band{background:var(--blue);color:var(--white);padding:0 6px;margin-right:4px}
.types-intro{left:12px;top:57px;width:225px;font-size:9.6px;line-height:1.25}
.types{left:12px;top:90px;width:235px;list-style:none}
.types li{font-size:13px;font-weight:700;color:var(--blue);line-height:1.25}
.types li::before{content:"●";font-size:9px;margin-right:2px}
.types span{display:block;font-weight:400;font-size:9.4px;color:var(--ink);padding-left:10px;line-height:1.2}
.rule{left:12px;top:338px;width:223px;height:4px;background:var(--grey-dark)}
.benefits-head{left:12px;top:352px;width:236px;font-size:14.2px;font-weight:700;color:var(--blue);line-height:1.28}
.benefits{left:12px;top:446px;width:238px;list-style:none}
.benefits li{font-size:9.1px;line-height:1.25;padding-left:8px;text-indent:-8px}
.benefits li::before{content:"●";font-size:7px;margin-right:1px}
.photo--hands{left:0;top:606px;width:240px;height:110px;background:linear-gradient(90deg,#f3efe8,#d8b898 55%,#b78a63)}
.process-head{left:248px;top:50px;width:308px;height:48px;background:var(--grey-dark);color:var(--white);font-weight:700;font-size:14px;padding:15px 0 0 12px}
.step{left:248px;width:308px;color:var(--white);padding:14px 8px 0 7px}
.step h3{font-size:14.5px;font-weight:700;line-height:1.1;margin-bottom:3px}
.step ul{list-style:none}
.step li{font-size:7.6px;line-height:1.22;padding-left:7px;text-indent:-7px}
.step li::before{content:"● ";font-size:6px}
.step--review{top:98px;height:158px;background:var(--blue-light)}
.step--proposal{top:256px;height:180px;background:var(--blue)}
.step--placement{top:436px;height:122px;background:var(--blue-bright)}
.notch--dark{border-top-color:var(--grey-dark);left:388px;top:97px}
.notch--review{border-top-color:var(--blue-light);left:388px;top:255px}
.notch--proposal{border-top-color:var(--blue);left:388px;top:435px}
.logo--back{left:248px;top:582px}
.address{left:248px;top:636px;font-size:8.4px;line-height:1.3;color:var(--grey-dark);font-style:normal}
</style>
</head>
<body>

<section class="page page--front">
  <svg class="curves" viewBox="0 0 556 716" aria-hidden="true">
    <path d="M300 0 C420 10 520 40 556 110 L556 90 C520 30 440 5 340 0Z" fill="#7a7a7a"/>
    <path d="M380 0 C470 15 535 45 556 80 L556 0Z" fill="#b9b9bb"/>
    <path d="M0 600 C60 660 170 700 300 716 L0 716Z" fill="#1f6fb2"/>
    <path d="M0 640 C70 690 160 710 240 716 L0 716Z" fill="#175a93"/>
  </svg>
  <h1 class="abs title">BUSINESS<span class="band">FINANCING</span>SERVICES</h1>
  <p class="abs cities">CALGARY &amp; VANCOUVER</p>
  <p class="abs intro">Financing is a key consideration for every business and is an integral part of allowing the business to properly plan for its future and realize its potential.</p>
  <div class="abs purpose-box">BUSINESSES REQUIRE FINANCING<br>FOR MANY PURPOSES, INCLUDING;</div>
  <ul class="abs purposes">
    <li><b>ASSET PURCHASES</b><span>(expand the capacity of your existing business by investing in equipment)</span></li>
    <li><b>WORKING CAPITAL</b><span>(helping to manage the short term cash flow pain that comes with increased business, usually from having to carry more inventory or a larger receivable balance from customers)</span></li>
    <li><b>GROWTH CAPITAL</b><span>(investing in expanding the your company's product or service offering)</span></li>
    <li><b>MERGERS &amp; ACQUISITIONS</b><span>(acquiring another company to increase the size or scale of your business)</span></li>
    <li><b>CORPORATE RESTRUCTURING<br>&nbsp;&nbsp;&nbsp;AND REFINANCING</b></li>
  </ul>
  <div class="abs logo logo--front"><span class="mark"></span><span class="name">RDK CHARTERED<br>PROFESSIONAL<br>ACCOUNTANTS</span></div>
  <div class="abs photo photo--desk" role="img" aria-label="Photo of business people reviewing financial charts at a desk with a laptop"></div>
  <div class="abs advisor">When considering financing alternatives it is <b>IMPORTANT TO HAVE AN ADVISOR THAT FULLY UNDERSTANDS YOUR COMPANY AND ITS NEEDS AS WELL AS THE MARKET</b> in order to ensure the following:</div>
  <div class="abs notch notch--advisor"></div>
  <ul class="abs goals">
    <li>Maximize The Probability of Obtaining The Optimal Financing</li>
    <li>The Right Amount of Financing</li>
    <li>The Most Favorable Terms</li>
    <li>The Most Reasonable Cost of Financing<span>(there are often fees associated with the transaction which must be considered in addition to the interest rate on a debt instrument)</span></li>
    <li>The Best Source of Financing<span>(lender or investor).</span></li>
  </ul>
</section>

<section class="page page--back">
  <svg class="curves" viewBox="0 0 556 716" aria-hidden="true">
    <path d="M250 716 C380 700 500 640 556 560 L556 600 C500 670 400 710 300 716Z" fill="#1f6fb2"/>
    <path d="M330 716 C430 700 520 660 556 620 L556 716Z" fill="#8a8a8a"/>
  </svg>
  <h2 class="abs types-head"><span class="band">FINANCING</span>TYPES</h2>
  <p class="abs types-intro">The types of financing used to meet financing needs might include:</p>
  <ul class="abs types">
    <li>Conventional Term Loans<span>(a loan that is paid back over a specific period of time, usually offered by one of the Big Banks)</span></li>
    <li>Operating Loans<span>(normally used for working capital, the balance usually fluctuates with the business</span></li>
    <li>Revolving Lines of Credit</li>
    <li>Project Financing<span>(secured and used to fund a very specific activity of the business)</span></li>
    <li>Factoring<span>(often used against accounts receivable in order to turn receivables to cash more quickly than simply waiting for the customer to pay)</span></li>
    <li>Subordinated Debt</li>
    <li>Venture Capital</li>
    <li>Angel Capital</li>
  </ul>
  <div class="abs rule"></div>
  <h2 class="abs benefits-head">WHAT ARE THE BENEFITS<br>OF USING RDK<br>TO GUIDE YOU THROUGH<br>THE FINANCING PROCESS?</h2>
  <ul class="abs benefits">
    <li>RDK's involvement using the above process enhances the chances of the client obtaining optimal financing.</li>
    <li>RDK's knowledge of, and relationships with, lenders and investors speeds up the financing process.</li>
    <li>RDK's analysis provides valuable insight into the client's present and projected circumstances and professional input to aid management in maximizing business performance and shareholder value.</li>
    <li>RDK's participation allows management to focus on other priorities.</li>
  </ul>
  <div class="abs photo photo--hands" role="img" aria-label="Photo of two hands joining puzzle pieces"></div>

  <h2 class="abs process-head">WHAT IS THE FINANCING PROCESS?</h2>
  <div class="abs step step--review">
    <h3>Review and Assessment of the Business</h3>
    <ul>
      <li>This step in the financing process involves obtaining and reviewing your financing package and supporting information, and interviewing you and possibly other key individuals.</li>
      <li>We assess your business and financing opportunity and the way they are presented, both from the perspective of how well they meet investor/ lender criteria and how compelling the proposal and presentation are.</li>
      <li>We identify strengths and weaknesses, and make specific recommendations to you as to how they might be addressed and your investment readiness improved.</li>
      <li>Armed with this assessment, you can proceed to structure and develop a financing proposal with increased confidence of financing success.</li>
    </ul>
  </div>
  <div class="abs step step--proposal">
    <h3>Developing a Financing Proposal</h3>
    <ul>
      <li>Developing a financing proposal involves considering and modeling alternate financing types and structures, and in some cases alternate corporate structures.</li>
      <li>RDK will work with you to weigh the pros and cons of each alternative.</li>
      <li>This analysis will then be used to identify the most suitable financing type and structure for your business.</li>
      <li>RDK will then prepare a Confidential Information Summary (CIS) in a format tailored for your financing opportunities.</li>
      <li>The CIS goes through the proposed transaction, addresses all relevant factors and provides the required supporting documentation.</li>
      <li>The CIS highlights the strengths of the proposal, explains how any weaknesses are mitigated, and conveys how your organization meets the prospective lender's or investor's criteria.</li>
      <li>Armed with the CIM, the financing placement process can begin.</li>
    </ul>
  </div>
  <div class="abs step step--placement">
    <h3>Financing Placement</h3>
    <ul>
      <li>Financing Placement involves: identifying and surveying prospective lenders and investors to determine the best sources of financing; presenting the proposal; and, monitoring and facilitating the information exchange process, negotiating between and communicating with the parties, and working towards a financing commitment with the best possible terms.</li>
    </ul>
  </div>
  <div class="abs notch notch--dark"></div>
  <div class="abs notch notch--review"></div>
  <div class="abs notch notch--proposal"></div>

  <div class="abs logo logo--back"><span class="mark"></span><span class="name">RDK CHARTERED<br>PROFESSIONAL<br>ACCOUNTANTS</span></div>
  <address class="abs address">4410-2080 Harlow Crescent SE<br>Calgary, AB, T2X 1A9<br>Phone: (403) 555-0142<br>Fax: (403) 555-0187</address>
</section>

</body>
</html>
```